General Contractors need a new Crisp updated Card Design

We need a new business card design for our company of 25 years based in Toronto call Holvaster Building Inc. : Our goal is to be the leading commercial contractors in Toronto by providing exceptional value to our clients. We work very hard to deliver professional, quality, service in conjunction with consistent price competitiveness to all of our clients on every single project.

Target Market(s)

Design & Build Clients

Industry/Entity Type

Construction Company

Contact Information for Business Card

Address:
18 North Tamlin Glen Road, Unit 57, Marbrook Vale, ON, K7T 2R9
Office: 905-218-5937

Holvasters Logo
Employee Job Description
Employee Cell Phone #
Employee Email
www.holvaster-example.com

Colors

Designer to choose colors to be used in the design.

Requirements
Must have
• Quote Company Saying:
• "Professional. Quality. Service."
Nice to have
• New Crisp up to date look. simple & fresh ( Not to Busy)
Should not have
• NO BLUE PRINTS ON THE BUSINESS CARDS

```html
<!DOCTYPE html>
<html lang="en">
<head>
<meta charset="utf-8">
<title>Holvaster Building Inc. — Business Card</title>
<link href="https://fonts.googleapis.com/css2?family=Nunito+Sans:ital,wght@0,400;0,700;0,800;1,400&display=swap" rel="stylesheet">
<style>
  :root {
    --teal: #03675e;
    --sage: #aabdb1;
    --mint-bg: #eff5f3;
    --card: #fdfdfd;
    --white: #ffffff;
  }
  * { box-sizing: border-box; margin: 0; padding: 0; }
  html, body {
    width: 1200px; height: 1200px; overflow: hidden;
    background: var(--white);
    font-family: "Nunito Sans", Arial, sans-serif;
  }
  .sheet {
    position: absolute; left: 132px; top: 0;
    width: 936px; height: 1200px;
    background: var(--mint-bg);
  }
  .card {
    position: absolute; left: 166px; width: 872px; height: 549px;
    background: var(--card);
  }
  .card--front { top: 38px; }
  .card--back { top: 608px; overflow: hidden; }

  .brand {
    position: absolute; left: 0; right: 0; top: 275px;
    display: flex; align-items: center; justify-content: center; gap: 16px;
  }
  .brand__mark { width: 34px; height: 34px; background: var(--teal); }
  .brand__name {
    color: var(--teal); font-weight: 800; font-size: 38px;
    letter-spacing: 1px; text-transform: uppercase;
  }
  .tagline {
    position: absolute; left: 0; right: 0; top: 484px;
    text-align: center; color: var(--teal);
    font-style: italic; font-size: 26px; letter-spacing: 0.3px;
  }

  .back__art {
    position: absolute; left: 0; top: 0; width: 440px; height: 549px;
    background: linear-gradient(160deg, var(--teal) 0%, var(--teal) 55%, var(--sage) 100%);
  }
  .back__panel {
    position: absolute; left: 440px; top: 0; width: 432px; height: 549px;
    background: var(--teal); color: var(--white);
    text-align: right; padding-right: 50px;
  }
  .person__name { margin-top: 88px; font-size: 30px; font-weight: 400; line-height: 1.2; }
  .person__name b { font-weight: 800; }
  .person__role { font-style: italic; font-size: 20px; margin-top: 2px; }
  .contact { margin-top: 40px; list-style: none; font-size: 19.5px; line-height: 30.5px; }
  .contact b { font-weight: 800; }
</style>
</head>
<body>
  <div class="sheet"></div>

  <section class="card card--front">
    <div class="brand">
      <span class="brand__mark"></span>
      <span class="brand__name">Holvaster Building Inc.</span>
    </div>
    <p class="tagline">Professional. Quality. Service.</p>
  </section>

  <section class="card card--back">
    <div class="back__art" role="img" aria-label="Large geometric brand decoration in teal and sage"></div>
    <div class="back__panel">
      <p class="person__name">Alex <b>Morrow</b></p>
      <p class="person__role">Position</p>
      <ul class="contact">
        <li><b>Address:</b> 18 North Tamlin Glen Road,</li>
        <li>Unit 57, Marbrook Vale, ON, K7T 2R9</li>
        <li><b>Office:</b> 905-218-5937</li>
        <li><b>Personal:</b> 097-381-642</li>
        <li><b>Email:</b> alexmorrow@holvaster-example.com</li>
        <li><b>Website:</b> www.holvaster-example.com</li>
      </ul>
    </div>
  </section>
</body>
</html>
```